Menu Board

Hi Marlene,

I would like you to design for me a menu board for all my products.

The layout I have hand drawn for you so just follow my layout.

Pho
Noodle salads
Rice
StirFry with Thick Rice Noodles
Spring Rolls Ricepaper Rolls

Poster Size: AO Vertical ( 841W x 1189H)

There are more photos of the rice dishes but I thought I can send this through so you can start and I can send you the rest of the photos when I get back from my photographer.

I will have items descriptions to follow also

• Here are the rest of the photos >

```html
<!DOCTYPE html>
<html lang="en">
<head>
<meta charset="utf-8">
<title>Lotus Lane – Menu Board</title>
<link rel="stylesheet" href="https://fonts.googleapis.com/css2?family=Bebas+Neue&family=Syncopate:wght@700&display=swap">
<style>
  :root {
    --bg-top: #414142;
    --bg-bottom: #252526;
    --orange: #f18a21;
    --orange-deep: #c9631b;
    --orange-light: #f6a623;
    --label: #ececec;
    --white: #ffffff;
    --plate: #f3f3f3;
    --plate-shade: #d9d9d9;
  }
  * { margin: 0; padding: 0; box-sizing: border-box; }
  html, body { width: 849px; height: 1200px; overflow: hidden; }
  body { background: var(--bg-bottom); }

  .menu-board {
    position: relative;
    width: 849px;
    height: 1200px;
    overflow: hidden;
    background: radial-gradient(ellipse 90% 60% at 45% 8%, var(--bg-top) 0%, #333334 45%, var(--bg-bottom) 100%);
  }
  .footer-wave { position: absolute; left: 0; top: 0; width: 849px; height: 1200px; }

  /* Brand */
  .brand {
    position: absolute;
    left: 50px; top: 114px;
    display: flex; align-items: center; gap: 9px;
  }
  .brand-dot { width: 12px; height: 12px; border-radius: 50%; background: var(--orange); }
  .brand-name {
    font-family: "Syncopate", sans-serif;
    font-weight: 700;
    font-size: 15px;
    color: var(--orange);
    letter-spacing: 1px;
  }

  /* Section banners */
  .banner { position: absolute; }
  .banner svg { position: absolute; left: 0; top: 0; overflow: visible; }
  .banner-title {
    position: absolute;
    left: 0; right: 0;
    font-family: "Syncopate", sans-serif;
    font-weight: 700;
    color: var(--white);
    text-align: center;
    letter-spacing: 3px;
  }

  /* Dish photo areas */
  .dish-photo {
    position: absolute;
    border-radius: 50% 50% 46% 46% / 34% 34% 66% 66%;
    box-shadow: 0 12px 16px rgba(0,0,0,0.4);
    background:
      radial-gradient(ellipse 78% 52% at 50% 30%, var(--c1) 0%, var(--c2) 42%, var(--c3) 68%, var(--plate) 71%, var(--plate-shade) 100%);
  }
  .round-photo {
    position: absolute;
    width: 180px; height: 180px;
    border-radius: 50%;
    background: radial-gradient(circle at 50% 62%, var(--c1) 0%, var(--c2) 40%, var(--c3) 100%);
  }

  .pho-beef      { --c1: #3e2412; --c2: #3f5e2a; --c3: #6b3b1c; }
  .pho-tofu      { --c1: #b8582a; --c2: #5e7a2e; --c3: #8a3f1a; }
  .pho-chicken   { --c1: #7a5530; --c2: #4d7a30; --c3: #9b6a3a; }
  .salad-beef    { --c1: #5a3420; --c2: #6e5234; --c3: #e2d6a8; }
  .salad-chicken { --c1: #c98a4a; --c2: #4f8a3a; --c3: #e08a3a; }
  .salad-pork    { --c1: #6a2e1a; --c2: #3f7a2e; --c3: #e8772c; }
  .salad-tofu    { --c1: #e0b060; --c2: #5a8a3a; --c3: #e8743a; }
  .spring-rolls  { --c1: #a85a22; --c2: #cf8a46; --c3: #f4eee8; }
  .rice-paper    { --c1: #8fbf5a; --c2: #e8efe0; --c3: #b98a58; }

  .dish-label {
    position: absolute;
    font-family: "Bebas Neue", sans-serif;
    font-size: 33px;
    line-height: 1;
    color: var(--label);
    letter-spacing: 0.5px;
    white-space: nowrap;
  }
</style>
</head>
<body>
<main class="menu-board">

  <svg class="footer-wave" viewBox="0 0 849 1200" aria-hidden="true">
    <defs>
      <linearGradient id="waveFill" x1="0" y1="0" x2="1" y2="0">
        <stop offset="0" stop-color="#d8611d"/>
        <stop offset="1" stop-color="#f6a623"/>
      </linearGradient>
    </defs>
    <path d="M0 1100 Q424 924 849 1100 L849 1200 L0 1200 Z" fill="url(#waveFill)"/>
  </svg>

  <header class="brand">
    <span class="brand-dot"></span>
    <span class="brand-name">LOTUS LANE</span>
  </header>

  <!-- Pho -->
  <div class="dish-photo pho-beef" role="img" aria-label="Bowl of beef pho" style="left:172px; top:168px; width:228px; height:152px;"></div>
  <div class="dish-photo pho-tofu" role="img" aria-label="Bowl of tofu pho" style="left:448px; top:134px; width:228px; height:150px;"></div>
  <div class="dish-photo pho-chicken" role="img" aria-label="Bowl of chicken pho" style="left:334px; top:228px; width:228px; height:150px;"></div>

  <div class="banner pho-banner" style="left:277px; top:74px; width:173px; height:110px;">
    <svg width="173" height="110" aria-hidden="true">
      <polygon points="70,70 124,70 122,108 100,106" fill="var(--orange-deep)"/>
      <polygon points="0,12 173,0 171,84 2,70" fill="var(--orange)"/>
    </svg>
    <span class="banner-title" style="top:24px; font-size:27px;">PHO</span>
  </div>

  <span class="dish-label" style="left:142px; top:288px;">BEEF</span>
  <span class="dish-label" style="left:266px; top:346px;">CHICKEN</span>
  <span class="dish-label" style="left:686px; top:182px;">TOFU</span>

  <!-- Noodle salad -->
  <div class="dish-photo salad-beef" role="img" aria-label="Beef noodle salad" style="left:60px; top:424px; width:204px; height:148px;"></div>
  <div class="dish-photo salad-chicken" role="img" aria-label="Chicken noodle salad" style="left:240px; top:424px; width:196px; height:148px;"></div>
  <div class="dish-photo salad-pork" role="img" aria-label="BBQ pork noodle salad" style="left:414px; top:424px; width:202px; height:148px;"></div>
  <div class="dish-photo salad-tofu" role="img" aria-label="Tofu noodle salad" style="left:598px; top:426px; width:214px; height:146px;"></div>

  <div class="banner salad-banner" style="left:550px; top:344px; width:242px; height:104px;">
    <svg width="242" height="104" aria-hidden="true">
      <polygon points="54,76 112,70 122,102" fill="var(--orange-deep)"/>
      <polygon points="0,8 240,0 242,78 2,68" fill="var(--orange)"/>
    </svg>
    <span class="banner-title" style="top:13px; font-size:23px; line-height:26px; letter-spacing:4px;">NOODLE<br>SALAD</span>
  </div>

  <span class="dish-label" style="left:144px; top:582px;">BEEF</span>
  <span class="dish-label" style="left:305px; top:582px;">CHICKEN</span>
  <span class="dish-label" style="left:473px; top:582px;">BBQ PORK</span>
  <span class="dish-label" style="left:681px; top:582px;">TOFU</span>

  <!-- Sides -->
  <div class="banner spring-banner" style="left:46px; top:898px; width:192px; height:86px;">
    <svg width="192" height="86" aria-hidden="true">
      <polygon points="58,62 150,62 146,84" fill="var(--orange-deep)"/>
      <polygon points="2,10 190,0 192,62 0,66" fill="var(--orange)"/>
    </svg>
    <span class="banner-title" style="top:13px; font-size:21px; line-height:25px;">SPRING<br>ROLLS</span>
  </div>
  <div class="banner rice-paper-banner" style="left:618px; top:870px; width:180px; height:144px;">
    <svg width="180" height="144" aria-hidden="true">
      <polygon points="40,92 116,92 110,122 54,142" fill="var(--orange-deep)"/>
      <polygon points="14,0 168,4 180,94 0,96" fill="var(--orange)"/>
    </svg>
    <span class="banner-title" style="top:13px; font-size:21px; line-height:25px;">RICE<br>PAPER<br>ROLLS</span>
  </div>

  <div class="round-photo spring-rolls" role="img" aria-label="Fried spring rolls with chilli dipping sauce" style="left:212px; top:918px;"></div>
  <div class="round-photo rice-paper" role="img" aria-label="Fresh rice paper rolls on a wooden board" style="left:456px; top:918px;"></div>

</main>
</body>
</html>
```